Postcard Design

Looking for 4.25 x6 postcard design for mass mailing
Design should be eye catching, energetic and draw the viewer in

Data for postcard to include:
Logo and slogan
Pediatric Occupational, Physical and Speech Therapy Services; Assistive Technology Evaluation and Training

Speech-Language Therapy
oral motor skills
speech delays
language skills
Articulation
Voice
fluency
cognitive skills
feeding disorders
Play skills

OCCUPATIONAL THERAPY
Our occupational therapists use play in therapy to help your child develop the skills he/she needs to perform their job of living and playing, including but not limited to:
- Increasing independence in self-care skills such as feeding, dressing and grooming
- Improving developmental skills such as rolling, sitting, standing
- Improving their sensory processing, balance, coordination and motor planning
- Difficulty tolerating clothing
- Poor balance - doesn't ride a bike/climb on slides, falls frequently, cries when moved unexpectedly
- Intolerance to textures/odors/loud sounds/movement
- Delayed handwriting and fine motor skills and/or
avoids fine motor activities such as using crayons, fasteners on clothing, pencils
- Limited diet-refuses to try new foods, gags when trying new tastes, textures
- Appears extremely anxious, states frequent fears of harmless things

CONTACT US TODAY for a FREE 15 minute consultation/Screen
(301) 555-4182
info@brightwillowkids.example
www.brightwillowkids.example

Physical therapy
Delayed crawling / walking
Persistent toe walking habits
Poor unsupported sitting/standing balance
Trouble learning how to jump, skip, ride a bike
Decreased ability to throw and catch a ball
Delayed motor milestones
Need for wheelchair mobility training
Balance coordination and motor planning difficulty
Strength , muscle tone and/ R range of motion impairment
Sports injuries
Postural control and positioning difficulty

```html
<!DOCTYPE html>
<html lang="en">
<head>
<meta charset="utf-8">
<title>Bright Willow Kids – Pediatric Therapy Postcard</title>
<link rel="stylesheet" href="https://fonts.googleapis.com/css2?family=Montserrat:wght@400;500;600;700;800;900&display=swap">
<style>
:root{
  --blue:#1a6fd4;
  --teal:#139a9c;
  --teal-light:#2bc0b6;
  --ink:#222428;
  --paper:#ffffff;
  --stage:#ebebeb;
  --grey:#cfd1d4;
}
*{box-sizing:border-box;margin:0;padding:0}
html,body{width:1200px;height:2295px;overflow:hidden}
body{background:var(--stage);font-family:"Montserrat",Arial,sans-serif;color:var(--ink);position:relative}
.postcard{position:absolute;left:50px;width:1100px;height:780px;background:var(--paper);box-shadow:0 6px 18px rgba(0,0,0,.18);overflow:hidden}
.postcard--front{top:317px}
.postcard--back{top:1197px}
.art{position:absolute;inset:0}
.brand{position:absolute;display:flex;align-items:center;gap:10px}
.brand__mark{width:30px;height:30px;border-radius:50%;background:var(--teal)}
.brand__name{font-weight:600;color:var(--blue);font-size:24px;line-height:1}
.front .brand{left:118px;top:66px}
.headline{position:absolute;left:114px;top:142px}
.headline__lead{font-weight:900;font-size:62px;color:var(--teal);line-height:1}
.headline__sub{font-weight:800;font-size:40px;color:var(--blue);line-height:1.05}
.headline__services{font-weight:700;font-size:22px;line-height:1.3;text-transform:uppercase;margin-top:6px}
.headline__semi{font-weight:500}
.headline__extra{font-weight:500;font-size:22px;line-height:1.3}
.service-list{position:absolute;list-style:none;color:#fff;font-weight:700;font-size:19px}
.service-list li{display:flex;gap:14px;margin-bottom:9px;line-height:1.2}
.tick{flex:none;width:18px;height:18px;margin-top:2px}
.service-list--a{left:115px;top:482px;width:240px}
.service-list--b{left:357px;top:484px;width:200px}
.cta{position:absolute;left:708px;top:0;width:380px;height:690px;font-weight:800;text-transform:uppercase}
.cta p{position:absolute;left:0;white-space:nowrap;line-height:1}
.cta__line{top:405px;font-size:38px}
.cta__big{top:440px;font-size:58px}
.cta__for{top:508px;font-weight:500;font-size:32px;color:var(--blue)}
.cta__free{top:532px;font-weight:900;font-size:98px;line-height:.9 !important;color:var(--teal-light);letter-spacing:-1px}
.cta__note{top:627px;left:14px !important;font-weight:700;font-size:20px;text-transform:none;line-height:1.15 !important}
.contact-bar{position:absolute;left:0;right:0;bottom:0;height:90px;display:flex;align-items:center;padding-left:110px}
.contact-bar__phone{display:flex;align-items:center;gap:12px;font-weight:800;font-size:54px}
.contact-bar__divider{width:2px;height:46px;background:var(--ink);margin:0 18px 0 20px}
.contact-bar__icons{display:flex;flex-direction:column;gap:4px;margin-right:18px}
.contact-bar__web{font-weight:700;font-size:21px;line-height:1.25}
.back-title{position:absolute;left:58px;top:42px;color:#fff;font-weight:800;line-height:1}
.back-title__small{font-size:41px}
.back-title__big{font-size:60px;font-weight:900}
.back-intro{position:absolute;left:58px;top:168px;width:460px;color:#fff;font-weight:700;font-size:12px;line-height:1.35}
.detail-list{position:absolute;list-style:none;color:#fff;font-size:11px;line-height:1.15}
.detail-list li{display:flex;gap:8px;margin-bottom:10px}
.detail-list .tick{width:12px;height:12px;margin-top:1px}
.detail-list--ot-a{left:58px;top:228px;width:220px}
.detail-list--ot-b{left:298px;top:232px;width:200px}
.detail-list--pt-a{left:58px;top:500px;width:230px}
.detail-list--pt-b{left:310px;top:500px;width:260px}
.detail-list--pt-a li,.detail-list--pt-b li{margin-bottom:7px}
.back .brand{left:588px;top:66px}
.back .brand__mark{width:22px;height:22px}
.back .brand__name{font-size:17px}
.stamp{position:absolute;left:916px;top:47px;width:124px;height:124px;background:var(--grey)}
.address-line{position:absolute;left:704px;width:330px;height:1px;background:#c9c9c9}
.back-phone{position:absolute;left:56px;top:708px;display:flex;align-items:center;gap:12px;font-weight:800;font-size:46px}
</style>
</head>
<body>

<section class="postcard postcard--front front" aria-label="Postcard front">
  <svg class="art" viewBox="0 0 1100 780">
    <defs>
      <linearGradient id="photoFade" x1="0" x2="1">
        <stop offset="0" stop-color="#ffffff"/>
        <stop offset=".25" stop-color="#eef0f1"/>
        <stop offset="1" stop-color="#d9d6d0"/>
      </linearGradient>
      <linearGradient id="domeTeal" x1="0" y1="0" x2="1" y2="1">
        <stop offset="0" stop-color="#16a3a1"/>
        <stop offset="1" stop-color="#0f8f98"/>
      </linearGradient>
      <linearGradient id="panelGrey" x1="0" y1="0" x2="0" y2="1">
        <stop offset="0" stop-color="#ffffff"/>
        <stop offset="1" stop-color="#c9cbcd"/>
      </linearGradient>
    </defs>
    <rect x="480" y="0" width="620" height="460" fill="url(#photoFade)" role="img" aria-label="Photo of a doctor and a mother with her toddler in a bright clinic"/>
    <path d="M540 690 Q700 330 905 320 Q1040 318 1100 410 L1100 690 Z" fill="var(--blue)"/>
    <path d="M595 690 Q735 375 915 365 Q1045 362 1100 445 L1100 690 Z" fill="url(#panelGrey)"/>
    <path d="M0 690 L0 600 Q140 365 330 362 Q560 360 745 690 Z" fill="url(#domeTeal)"/>
    <path d="M12 610 Q150 395 330 392 Q545 392 715 690" fill="none" stroke="#ffffff" stroke-opacity=".55" stroke-width="2"/>
    <rect x="0" y="690" width="1100" height="90" fill="#ffffff"/>
  </svg>

  <div class="brand"><span class="brand__mark"></span><span class="brand__name">Bright Willow Kids</span></div>

  <div class="headline">
    <p class="headline__lead">PEDIATRIC</p>
    <p class="headline__sub">OCCUPATIONAL,</p>
    <p class="headline__services">Physical and Speech<br>Therapy Services<span class="headline__semi">;</span></p>
    <p class="headline__extra">Assistive Technology Evaluation<br>and Training</p>
  </div>

  <ul class="service-list service-list--a">
    <li><svg class="tick" viewBox="0 0 20 20"><circle cx="10" cy="10" r="10" fill="#fff"/><path d="M5.5 10.5l3 3 6-6.5" fill="none" stroke="var(--teal)" stroke-width="2.4"/></svg>Speech-Language Therapy</li>
    <li><svg class="tick" viewBox="0 0 20 20"><circle cx="10" cy="10" r="10" fill="#fff"/><path d="M5.5 10.5l3 3 6-6.5" fill="none" stroke="var(--teal)" stroke-width="2.4"/></svg>oral motor skills</li>
    <li><svg class="tick" viewBox="0 0 20 20"><circle cx="10" cy="10" r="10" fill="#fff"/><path d="M5.5 10.5l3 3 6-6.5" fill="none" stroke="var(--teal)" stroke-width="2.4"/></svg>speech delays</li>
    <li><svg class="tick" viewBox="0 0 20 20"><circle cx="10" cy="10" r="10" fill="#fff"/><path d="M5.5 10.5l3 3 6-6.5" fill="none" stroke="var(--teal)" stroke-width="2.4"/></svg>language skills</li>
    <li><svg class="tick" viewBox="0 0 20 20"><circle cx="10" cy="10" r="10" fill="#fff"/><path d="M5.5 10.5l3 3 6-6.5" fill="none" stroke="var(--teal)" stroke-width="2.4"/></svg>Articulation</li>
  </ul>
  <ul class="service-list service-list--b">
    <li><svg class="tick" viewBox="0 0 20 20"><circle cx="10" cy="10" r="10" fill="#fff"/><path d="M5.5 10.5l3 3 6-6.5" fill="none" stroke="var(--teal)" stroke-width="2.4"/></svg>Voice<br>fluency</li>
    <li><svg class="tick" viewBox="0 0 20 20"><circle cx="10" cy="10" r="10" fill="#fff"/><path d="M5.5 10.5l3 3 6-6.5" fill="none" stroke="var(--teal)" stroke-width="2.4"/></svg>cognitive skills</li>
    <li><svg class="tick" viewBox="0 0 20 20"><circle cx="10" cy="10" r="10" fill="#fff"/><path d="M5.5 10.5l3 3 6-6.5" fill="none" stroke="var(--teal)" stroke-width="2.4"/></svg>feeding disorders</li>
    <li><svg class="tick" viewBox="0 0 20 20"><circle cx="10" cy="10" r="10" fill="#fff"/><path d="M5.5 10.5l3 3 6-6.5" fill="none" stroke="var(--teal)" stroke-width="2.4"/></svg>Play skills</li>
  </ul>

  <div class="cta">
    <p class="cta__line">Contact us</p>
    <p class="cta__big">Today!!</p>
    <p class="cta__for">For a</p>
    <p class="cta__free">FREE</p>
    <p class="cta__note">15 minute consultation/<br>&nbsp;Screen</p>
  </div>

  <div class="contact-bar">
    <div class="contact-bar__phone">
      <svg width="32" height="32" viewBox="0 0 24 24"><path d="M6.6 10.8a15 15 0 006.6 6.6l2.2-2.2a1 1 0 011-.25 11.4 11.4 0 003.6.6 1 1 0 011 1V20a1 1 0 01-1 1A17 17 0 013 4a1 1 0 011-1h3.5a1 1 0 011 1 11.4 11.4 0 00.6 3.6 1 1 0 01-.25 1z" fill="var(--blue)"/></svg>
      (301) 555-4182
    </div>
    <span class="contact-bar__divider"></span>
    <div class="contact-bar__icons">
      <svg width="18" height="16" viewBox="0 0 18 16"><rect x="1" y="2" width="16" height="12" rx="1" fill="none" stroke="var(--blue)" stroke-width="2"/><path d="M1 3l8 6 8-6" fill="none" stroke="var(--blue)" stroke-width="2"/></svg>
      <svg width="18" height="18" viewBox="0 0 18 18"><circle cx="9" cy="9" r="7.5" fill="none" stroke="var(--blue)" stroke-width="2"/><path d="M1.5 9h15M9 1.5c-4 4.5-4 10.5 0 15M9 1.5c4 4.5 4 10.5 0 15" fill="none" stroke="var(--blue)" stroke-width="1.5"/></svg>
    </div>
    <p class="contact-bar__web">info@brightwillowkids.example<br>www.brightwillowkids.example</p>
  </div>
</section>

<section class="postcard postcard--back back" aria-label="Postcard back">
  <svg class="art" viewBox="0 0 1100 780">
    <defs>
      <clipPath id="backPanel"><path d="M0 0 H385 C640 80 720 400 600 690 H0 Z"/></clipPath>
    </defs>
    <path d="M400 0 C665 85 745 400 625 690" fill="none" stroke="var(--teal)" stroke-width="7"/>
    <path d="M0 0 H385 C640 80 720 400 600 690 H0 Z" fill="var(--blue)"/>
    <rect x="0" y="480" width="1100" height="210" fill="var(--teal)" clip-path="url(#backPanel)"/>
  </svg>

  <div class="back-title">
    <p class="back-title__small">OCCUPATIONAL</p>
    <p class="back-title__big">THERAPY</p>
  </div>
  <p class="back-intro">Our occupational therapists use play in therapy to help your child develop the skills he/she needs to perform their job of living and playing, including but not limited to:</p>

  <ul class="detail-list detail-list--ot-a">
    <li><svg class="tick" viewBox="0 0 20 20"><circle cx="10" cy="10" r="10" fill="#fff"/><path d="M5.5 10.5l3 3 6-6.5" fill="none" stroke="var(--blue)" stroke-width="2.6"/></svg>Increasing independence in self-care skills such as feeding, dressing and grooming</li>
    <li><svg class="tick" viewBox="0 0 20 20"><circle cx="10" cy="10" r="10" fill="#fff"/><path d="M5.5 10.5l3 3 6-6.5" fill="none" stroke="var(--blue)" stroke-width="2.6"/></svg>Improving developmental skills such as rolling, sitting, standing</li>
    <li><svg class="tick" viewBox="0 0 20 20"><circle cx="10" cy="10" r="10" fill="#fff"/><path d="M5.5 10.5l3 3 6-6.5" fill="none" stroke="var(--blue)" stroke-width="2.6"/></svg>Improving their sensory processing, balance, coordination and motor planning</li>
    <li><svg class="tick" viewBox="0 0 20 20"><circle cx="10" cy="10" r="10" fill="#fff"/><path d="M5.5 10.5l3 3 6-6.5" fill="none" stroke="var(--blue)" stroke-width="2.6"/></svg>Difficulty tolerating clothing</li>
    <li><svg class="tick" viewBox="0 0 20 20"><circle cx="10" cy="10" r="10" fill="#fff"/><path d="M5.5 10.5l3 3 6-6.5" fill="none" stroke="var(--blue)" stroke-width="2.6"/></svg>Poor balance - doesn't ride a bike/climb on slides, falls frequently, cries when moved unexpectedly</li>
  </ul>
  <ul class="detail-list detail-list--ot-b">
    <li><svg class="tick" viewBox="0 0 20 20"><circle cx="10" cy="10" r="10" fill="#fff"/><path d="M5.5 10.5l3 3 6-6.5" fill="none" stroke="var(--blue)" stroke-width="2.6"/></svg>Intolerance to textures/odors /loud sounds/movement</li>
    <li><svg class="tick" viewBox="0 0 20 20"><circle cx="10" cy="10" r="10" fill="#fff"/><path d="M5.5 10.5l3 3 6-6.5" fill="none" stroke="var(--blue)" stroke-width="2.6"/></svg>Delayed handwriting and fine motor skills and/or avoids fine motor activities such as using crayons, fasteners on clothing, pencils</li>
    <li><svg class="tick" viewBox="0 0 20 20"><circle cx="10" cy="10" r="10" fill="#fff"/><path d="M5.5 10.5l3 3 6-6.5" fill="none" stroke="var(--blue)" stroke-width="2.6"/></svg>Limited diet-refuses to try new foods, gags when trying new tastes, textures</li>
    <li><svg class="tick" viewBox="0 0 20 20"><circle cx="10" cy="10" r="10" fill="#fff"/><path d="M5.5 10.5l3 3 6-6.5" fill="none" stroke="var(--blue)" stroke-width="2.6"/></svg>Appears extremely anxious, states frequent fears of harmless things</li>
  </ul>

  <ul class="detail-list detail-list--pt-a">
    <li><svg class="tick" viewBox="0 0 20 20"><circle cx="10" cy="10" r="10" fill="#fff"/><path d="M5.5 10.5l3 3 6-6.5" fill="none" stroke="var(--teal)" stroke-width="2.6"/></svg>Physical therapy</li>
    <li><svg class="tick" viewBox="0 0 20 20"><circle cx="10" cy="10" r="10" fill="#fff"/><path d="M5.5 10.5l3 3 6-6.5" fill="none" stroke="var(--teal)" stroke-width="2.6"/></svg>Delayed crawling / walking</li>
    <li><svg class="tick" viewBox="0 0 20 20"><circle cx="10" cy="10" r="10" fill="#fff"/><path d="M5.5 10.5l3 3 6-6.5" fill="none" stroke="var(--teal)" stroke-width="2.6"/></svg>Persistent toe walking habits</li>
    <li><svg class="tick" viewBox="0 0 20 20"><circle cx="10" cy="10" r="10" fill="#fff"/><path d="M5.5 10.5l3 3 6-6.5" fill="none" stroke="var(--teal)" stroke-width="2.6"/></svg>Poor unsupported sitting/ standing balance</li>
    <li><svg class="tick" viewBox="0 0 20 20"><circle cx="10" cy="10" r="10" fill="#fff"/><path d="M5.5 10.5l3 3 6-6.5" fill="none" stroke="var(--teal)" stroke-width="2.6"/></svg>Trouble learning how to jump, skip, ride a bike</li>
    <li><svg class="tick" viewBox="0 0 20 20"><circle cx="10" cy="10" r="10" fill="#fff"/><path d="M5.5 10.5l3 3 6-6.5" fill="none" stroke="var(--teal)" stroke-width="2.6"/></svg>Decreased ability to throw and catch a ball</li>
    <li><svg class="tick" viewBox="0 0 20 20"><circle cx="10" cy="10" r="10" fill="#fff"/><path d="M5.5 10.5l3 3 6-6.5" fill="none" stroke="var(--teal)" stroke-width="2.6"/></svg>Delayed motor milestones</li>
  </ul>
  <ul class="detail-list detail-list--pt-b">
    <li><svg class="tick" viewBox="0 0 20 20"><circle cx="10" cy="10" r="10" fill="#fff"/><path d="M5.5 10.5l3 3 6-6.5" fill="none" stroke="var(--teal)" stroke-width="2.6"/></svg>Need for wheelchair mobility training</li>
    <li><svg class="tick" viewBox="0 0 20 20"><circle cx="10" cy="10" r="10" fill="#fff"/><path d="M5.5 10.5l3 3 6-6.5" fill="none" stroke="var(--teal)" stroke-width="2.6"/></svg>Balance coordination and motor planning difficulty</li>
    <li><svg class="tick" viewBox="0 0 20 20"><circle cx="10" cy="10" r="10" fill="#fff"/><path d="M5.5 10.5l3 3 6-6.5" fill="none" stroke="var(--teal)" stroke-width="2.6"/></svg>Strength , muscle tone and/ R range of motion impairment</li>
    <li><svg class="tick" viewBox="0 0 20 20"><circle cx="10" cy="10" r="10" fill="#fff"/><path d="M5.5 10.5l3 3 6-6.5" fill="none" stroke="var(--teal)" stroke-width="2.6"/></svg>Sports injuries</li>
    <li><svg class="tick" viewBox="0 0 20 20"><circle cx="10" cy="10" r="10" fill="#fff"/><path d="M5.5 10.5l3 3 6-6.5" fill="none" stroke="var(--teal)" stroke-width="2.6"/></svg>Postural control and positioning difficulty</li>
  </ul>

  <div class="brand"><span class="brand__mark"></span><span class="brand__name">Bright Willow Kids</span></div>
  <div class="stamp"></div>
  <span class="address-line" style="top:310px"></span>
  <span class="address-line" style="top:378px"></span>
  <span class="address-line" style="top:448px"></span>
  <span class="address-line" style="top:522px"></span>

  <div class="back-phone">
    <svg width="30" height="30" viewBox="0 0 24 24"><path d="M6.6 10.8a15 15 0 006.6 6.6l2.2-2.2a1 1 0 011-.25 11.4 11.4 0 003.6.6 1 1 0 011 1V20a1 1 0 01-1 1A17 17 0 013 4a1 1 0 011-1h3.5a1 1 0 011 1 11.4 11.4 0 00.6 3.6 1 1 0 01-.25 1z" fill="var(--blue)"/></svg>
    (301) 555-4182
  </div>
</section>

</body>
</html>
```